Wine Shop Banners

Banner graphic/images required
Require banner images to match the present online wine shop.

www.korbel-traube-laden.de

The wine-shop presently has a very clean, simple design, lots of white space, which is very much the trend at the moment.

Requirements
Images or graphic design for present banners visible on the homepage

The colour and feeling of the banners must fit in with the present clean, simple design.

Work required
3 large slide-card/banners (can be more) and 3 smaller fixed banners below. Please view website to see present position of banners.

LARGE BANNERS x 3

Something special with white background within the banner space
White background on each slide-card. Small individual graphic image in the middle of the slide card. This could be either a simple element of wine:
ingredients, fruit (grape), bottle, cork, old bottle label etc. just displaying one item on each slide-card. Preferably with high quality graphic features.

Note:
We are trying the steer away from the classic stereotype wineshop design. The image/s should have a higher, individual graphic touch, which gives the design something different. Sometimes such artistic work is displayed in steampunk or even in nostalgic design, which leaves the viewer slightly memorized with the content.
To clarify: we are not looking for a full steampunk design but possibly certain elements of this will give you an idea what we mean. That is to say, the design can go slightly in this direction without going over the top. Something small but very eye-catching.

SMALLER BANNERS x 3

One idea is:
Showing a symbol e.g. - discount sign "%" against a white background but again with a high graphic quality.

Target Market(s)

People interested in purchasing wine.
Ages approx. 25 to 65

Industry/Entity Type

Shop

Requirements
Must have
• Something special with white background
• Small individual graphic image in the middle of the slide card.
Nice to have
• The image/s should have a higher, individual graphic touch, which gives the design something different. Something that leaves the viewer slightly memorized with the content.
Should not have
• Not the typical classical design that is often seen on wine shops.

```html
<!DOCTYPE html>
<html lang="en">
<head>
<meta charset="utf-8">
<title>Royal Quality Wine – Banner</title>
<link rel="stylesheet" href="https://fonts.googleapis.com/css2?family=Cormorant+Garamond:wght@500&family=Lato:wght@300&display=swap">
<style>
  :root {
    --paper: #ffffff;
    --band: #eeece7;
    --title-green: #7f9a5a;
    --text-grey: #8a8784;
    --plum: #4a3a4c;
    --lime: #bcd24a;
    --cellar-dark: #3b2a22;
    --cellar-mid: #5e4233;
    --cellar-warm: #7a5038;
    --grape-tint: #ece9e1;
  }
  * { margin: 0; padding: 0; box-sizing: border-box; }
  html, body { width: 1200px; height: 467px; overflow: hidden; background: var(--paper); }
  .banner { position: relative; width: 1200px; height: 467px; background: var(--paper); overflow: hidden; }
  .banner__shapes { position: absolute; inset: 0; }
  .title-band {
    position: absolute; left: 450px; top: 68px; width: 750px; height: 85px;
    background: var(--band);
  }
  .title {
    position: absolute; left: 450px; top: 68px; width: 780px; height: 85px;
    display: flex; align-items: center; justify-content: center;
    font-family: "Cormorant Garamond", serif; font-weight: 500;
    font-size: 62px; letter-spacing: 0.5px; color: var(--title-green);
    white-space: nowrap; padding-top: 4px;
  }
  .tagline {
    position: absolute; left: 616px; top: 203px; width: 484px;
    text-align: center; font-family: "Lato", sans-serif; font-weight: 300;
    font-size: 33px; line-height: 45.5px; color: var(--text-grey);
    text-transform: uppercase; letter-spacing: 0.3px;
  }
  .tagline-shadow {
    position: absolute; left: 695px; top: 393px; width: 325px; height: 12px;
    border-radius: 50%;
    background: radial-gradient(ellipse at center, rgba(0,0,0,0.09), rgba(0,0,0,0) 70%);
  }
</style>
</head>
<body>
<main class="banner">
  <svg class="banner__shapes" width="1200" height="467" viewBox="0 0 1200 467">
    <defs>
      <linearGradient id="cellar" x1="0" y1="0" x2="1" y2="1">
        <stop offset="0" stop-color="var(--cellar-mid)"/>
        <stop offset="0.45" stop-color="var(--cellar-warm)"/>
        <stop offset="1" stop-color="var(--cellar-dark)"/>
      </linearGradient>
      <radialGradient id="grapes" cx="0.65" cy="0.7" r="0.7">
        <stop offset="0" stop-color="var(--grape-tint)"/>
        <stop offset="0.6" stop-color="var(--grape-tint)" stop-opacity="0.5"/>
        <stop offset="1" stop-color="#ffffff" stop-opacity="0"/>
      </radialGradient>
    </defs>
    <polygon class="photo-area" role="img" aria-label="Photo of a man in a wine cellar smelling red wine in a glass"
             points="0,0 376,0 567,467 0,467" fill="url(#cellar)"/>
    <rect class="grape-decoration" role="img" aria-label="Faint line drawing of a grape bunch with leaves"
          x="970" y="229" width="230" height="238" fill="url(#grapes)"/>
    <polygon class="accent-plum" points="376,0 408,0 599,467 567,467" fill="var(--plum)"/>
    <polygon class="accent-lime" points="408,0 420,0 611,467 599,467" fill="var(--lime)"/>
  </svg>
  <div class="title-band"></div>
  <h1 class="title">ROYAL QUALITY WINE</h1>
  <p class="tagline">Let yourself<br>be surprised by<br>the quality and<br>taste of our wines</p>
  <div class="tagline-shadow"></div>
</main>
</body>
</html>
```